Quotation (Proposal) Form

We are looking for a redesign of an existing form - one that fits our new marketing material better and, frankly, a form that looks a lot nicer than the boring form we use today. 8.5"x11". CMYK. Minimum 300 dpi necessary for printing. I have attached our current quote form as well as some other designs that show the direction we are going in. Please note, that this has to be able to have our people manually write in pen on it when we provide it to potential customers. Thank you!

Target Market(s)

Residential homeowners

Industry/Entity Type

Snow Removal

Font styles to use
Sans Serif

Colors

Designer to choose colors to be used in the design.

Requirements
Must have
• Should be easy to read and look great. Should also add the following text - "Exclusively serving Northeast Grand Rapids and suburbs"
Nice to have
• Similar concept to other marketing material we have done (attached). Easy to read. Professional.
Should not have
• Cluttered look. Unevenly spaced.

```html
<!DOCTYPE html>
<html lang="en">
<head>
<meta charset="utf-8">
<title>Birch Hollow Snowplowing – Seasonal Quote</title>
<link href="https://fonts.googleapis.com/css2?family=Montserrat:wght@400;500;600;700;800&display=swap" rel="stylesheet">
<style>
  :root{
    --backdrop:#262828;
    --paper:#f1f1f1;
    --green:#1f7a33;
    --green-dark:#14632a;
    --ink:#1e1e1e;
    --charcoal:#2b2b2b;
    --panel-light:#e6e6e6;
    --panel-dark:#bdbdbd;
    --rule:#8a8a8a;
    --white:#ffffff;
  }
  *{box-sizing:border-box;margin:0;padding:0}
  html,body{width:1200px;height:1200px;overflow:hidden;background:var(--backdrop)}
  body{font-family:"Montserrat",sans-serif;color:var(--ink);position:relative}
  .sheet{position:absolute;left:186px;top:20px;width:828px;height:1160px;
    background:linear-gradient(180deg,#f6f6f6,#e9e9e9);overflow:hidden}
  .hero{position:absolute;left:0;top:0;width:828px;height:480px}
  .hero-photo{position:absolute;left:0;top:0;width:828px;height:470px;
    background:
      radial-gradient(ellipse 260px 160px at 300px 230px,rgba(214,88,38,.55),transparent 70%),
      radial-gradient(ellipse 330px 200px at 620px 140px,rgba(235,240,246,.9),transparent 70%),
      linear-gradient(180deg,#4a4234 0%,#5d5a4d 22%,#9aa3a8 45%,#d7dee6 70%,#eef2f6 100%)}
  .contact-card{position:absolute;left:415px;top:149px;width:385px;height:300px;
    border-radius:18px;background:linear-gradient(180deg,var(--panel-light),var(--panel-dark));
    padding:26px 20px 0 18px}
  .field{display:flex;align-items:flex-end;height:45px;font-size:16.5px;font-weight:500;color:var(--ink)}
  .field .line{flex:1;border-bottom:1px solid var(--rule);margin-left:10px;margin-bottom:5px}
  .field .line.short{flex:0 0 160px}
  .field .label-zip{margin-left:10px}
  .hero-wave{position:absolute;left:0;top:0}
  .brand-badge{position:absolute;left:60px;top:249px;width:214px;height:214px;border-radius:50%;
    background:var(--white);border:4px solid var(--green);display:flex;flex-direction:column;
    align-items:center;justify-content:center;text-align:center}
  .brand-name{font-size:25px;font-weight:700;color:var(--charcoal);line-height:1.2}
  .title-row{position:absolute;left:76px;top:483px;width:665px;height:35px;display:flex;align-items:center}
  .title-row .rule{height:4px;background:var(--charcoal)}
  .title-pill{background:var(--green);color:var(--white);height:35px;border-radius:18px;
    font-weight:800;font-size:22px;letter-spacing:.4px;display:flex;align-items:center;justify-content:center;
    width:545px;margin:0 6px}
  .terms{position:absolute;left:30px;top:539px;list-style:none}
  .terms li{display:flex;align-items:flex-start;font-size:13.6px;font-weight:600;line-height:16px;min-height:32.5px}
  .terms svg{flex:0 0 20px;margin-right:8px;margin-top:-1px}
  .payment{position:absolute;left:56px;display:flex;align-items:center;font-size:14.5px;font-weight:500}
  .payment .amount-box{width:141px;height:37px;border:2.5px solid var(--charcoal);border-radius:19px;margin-left:24px;background:var(--white)}
  .payment.one{top:885px}
  .payment.two{top:935px}
  .footer-wave{position:absolute;left:0;top:960px}
  .signoff{position:absolute;left:60px;top:993px;width:369px;height:135px;border-radius:16px;
    background:linear-gradient(180deg,#dadada,#bdbdbd);border-top:4px solid var(--charcoal);border-left:4px solid var(--charcoal);
    padding:18px 24px 0 26px}
  .signoff h2{font-size:11.8px;font-weight:600;letter-spacing:.2px;white-space:nowrap;padding-bottom:8px;border-bottom:1.5px solid #555}
  .signoff .sig-row{display:flex;font-size:12.6px;font-weight:600;margin-top:18px}
  .signoff .sig-row span:first-child{width:235px}
  .contact{position:absolute;right:30px;color:var(--white);display:flex;align-items:center;font-weight:500;white-space:nowrap}
  .contact svg{margin-right:10px}
  .contact.phone{top:1040px;font-size:14.5px}
  .contact.email{top:1068px;font-size:14.5px}
  .contact.address{top:1097px;font-size:11.5px}
  .service-area{position:absolute;right:30px;top:1124px;color:var(--white);font-size:12.5px;font-weight:700;letter-spacing:.2px;white-space:nowrap}
</style>
</head>
<body>
<main class="sheet">
  <section class="hero">
    <div class="hero-photo" role="img" aria-label="Photo of an orange snowplow truck throwing snow off a wintry road beside a pine forest"></div>
    <form class="contact-card">
      <div class="field">Name<span class="line"></span></div>
      <div class="field">Address<span class="line"></span></div>
      <div class="field">Phone<span class="line"></span></div>
      <div class="field">City<span class="line short"></span><span class="label-zip">Zip</span><span class="line"></span></div>
      <div class="field">Email Address<span class="line"></span></div>
    </form>
    <svg class="hero-wave" width="828" height="480" viewBox="0 0 828 480">
      <path d="M0,388 C220,356 420,456 620,432 C710,422 780,396 828,368 L828,480 L0,480Z" fill="#2b2b2b"/>
      <path d="M0,396 C220,364 420,464 620,440 C710,430 780,402 828,376 L828,480 L0,480Z" fill="#1f7a33"/>
      <path d="M0,410 C220,380 420,474 620,452 C710,442 780,416 828,392 L828,480 L0,480Z" fill="#f5f5f5"/>
    </svg>
    <div class="brand-badge"><span class="brand-name">Birch Hollow<br>Snowplowing</span></div>
  </section>

  <div class="title-row">
    <span class="rule" style="width:59px"></span>
    <h1 class="title-pill">UNLIMITED PLOWING SEASONAL QUOTE</h1>
    <span class="rule" style="width:49px"></span>
  </div>

  <ul class="terms">
    <li><svg width="20" height="18" viewBox="0 0 20 18"><path d="M2 10 L7 15 L18 2" fill="none" stroke="#1f7a33" stroke-width="3.4" stroke-linecap="round"/></svg>Birch Hollow is a fully licensed and insured snow removal service.</li>
    <li><svg width="20" height="18" viewBox="0 0 20 18"><path d="M2 10 L7 15 L18 2" fill="none" stroke="#1f7a33" stroke-width="3.4" stroke-linecap="round"/></svg>Plowing will be done when snow has accumulated 1" or more.</li>
    <li><svg width="20" height="18" viewBox="0 0 20 18"><path d="M2 10 L7 15 L18 2" fill="none" stroke="#1f7a33" stroke-width="3.4" stroke-linecap="round"/></svg>24 hour phone availability during snow events.</li>
    <li><svg width="20" height="18" viewBox="0 0 20 18"><path d="M2 10 L7 15 L18 2" fill="none" stroke="#1f7a33" stroke-width="3.4" stroke-linecap="round"/></svg>Hard rubber plow edges protect concrete and pavement from scratches and rust marks.</li>
    <li><svg width="20" height="18" viewBox="0 0 20 18"><path d="M2 10 L7 15 L18 2" fill="none" stroke="#1f7a33" stroke-width="3.4" stroke-linecap="round"/></svg>Snow will be removed by 6:00 AM depending upon time and amount.</li>
    <li><svg width="20" height="18" viewBox="0 0 20 18"><path d="M2 10 L7 15 L18 2" fill="none" stroke="#1f7a33" stroke-width="3.4" stroke-linecap="round"/></svg>Hand shoveling of walkways/front patios available.</li>
    <li><svg width="20" height="18" viewBox="0 0 20 18"><path d="M2 10 L7 15 L18 2" fill="none" stroke="#1f7a33" stroke-width="3.4" stroke-linecap="round"/></svg>Salting of driveways available.</li>
    <li><svg width="20" height="18" viewBox="0 0 20 18"><path d="M2 10 L7 15 L18 2" fill="none" stroke="#1f7a33" stroke-width="3.4" stroke-linecap="round"/></svg>We will return to clean the approach of your drive after the city plows your street.</li>
    <li><svg width="20" height="18" viewBox="0 0 20 18"><path d="M2 10 L7 15 L18 2" fill="none" stroke="#1f7a33" stroke-width="3.4" stroke-linecap="round"/></svg>A slip-free surface can't be guaranteed.</li>
    <li><svg width="20" height="18" viewBox="0 0 20 18"><path d="M2 10 L7 15 L18 2" fill="none" stroke="#1f7a33" stroke-width="3.4" stroke-linecap="round"/></svg>Email-based snow event information and real time<br>updates provided to customers</li>
  </ul>

  <div class="payment one">One payment due by October 31<span class="amount-box"></span></div>
  <div class="payment two">Two equal installments due by October 31 &amp; December 31<span class="amount-box"></span></div>

  <svg class="footer-wave" width="828" height="200" viewBox="0 0 828 200">
    <path d="M0,48 C120,20 240,92 430,84 C600,76 700,24 828,36 L828,200 L0,200Z" fill="#2b2b2b"/>
    <path d="M0,56 C120,30 240,100 430,92 C600,84 700,34 828,44 L828,200 L0,200Z" fill="#1f7a33"/>
  </svg>

  <section class="signoff">
    <h2>PLEASE SIGN &amp; RETURN COPY WITH PAYMENT</h2>
    <div class="sig-row"><span>Birch Hollow:</span><span>Date:</span></div>
    <div class="sig-row"><span>Customer:</span><span>Date:</span></div>
  </section>

  <div class="contact phone"><svg width="16" height="16" viewBox="0 0 24 24"><path d="M6.6 10.8a15 15 0 0 0 6.6 6.6l2.2-2.2a1 1 0 0 1 1-.25 11.4 11.4 0 0 0 3.6.57 1 1 0 0 1 1 1V20a1 1 0 0 1-1 1A17 17 0 0 1 3 4a1 1 0 0 1 1-1h3.5a1 1 0 0 1 1 1c0 1.250.2 2.45.57 3.57a1 1 0 0 1-.25 1z" fill="#fff"/></svg>(555) 014-2290</div>
  <div class="contact email"><svg width="22" height="16" viewBox="0 0 22 16"><rect x="1" y="1" width="20" height="14" fill="none" stroke="#fff" stroke-width="1.6"/><path d="M1 1 L11 9 L21 1" fill="none" stroke="#fff" stroke-width="1.6"/></svg>hello@birchhollowplow.com</div>
  <div class="contact address"><svg width="16" height="20" viewBox="0 0 16 20"><path d="M8 0a7 7 0 0 0-7 7c0 5 7 13 7 13s7-8 7-13a7 7 0 0 0-7-7zm0 10a3 3 0 1 1 0-6 3 3 0 0 1 0 6z" fill="#fff"/></svg>1480 Maple Ridge Lane NE Grand Rapids, MI 49505</div>
  <p class="service-area">Exclusively serving Northeast Grand Rapids and suburbs</p>
</main>
</body>
</html>
```